Bref créative
Real Estate Development Firm
Marlow Holdings
I need double sided standard sized Business Card [3.5" x 2"]
May use same font as in logo or other suggestions
Professional
Derek P. Hollins
President/CEO
248 West Penrose Street
Suite 2360
Milwaukee, WI 53217
dhollins@marlowholdingsllc.example
marlowholdingsllc.example
You can refer to logo design contest for other ideas.
Logo and design or color gradient or other suggestions.
Please use logo

```html
<!DOCTYPE html>
<html lang="en">
<head>
<meta charset="UTF-8">
<title>Marlow Holdings Business Card</title>
<link href="https://fonts.googleapis.com/css2?family=Cinzel:wght@400;600&display=swap" rel="stylesheet">
<style>
  :root {
    --canvas-bg: #7a7a7a;
    --card-top: #ffffff;
    --card-bottom: #dcdcdc;
    --brand-blue: #26357a;
    --ink: #2f2f2f;
    --ink-soft: #4a4a4a;
  }
  * { margin: 0; padding: 0; box-sizing: border-box; }
  html, body {
    width: 1200px;
    height: 996px;
    overflow: hidden;
  }
  body {
    background: var(--canvas-bg);
    font-family: "Cinzel", "Times New Roman", serif;
    display: flex;
    flex-direction: column;
    align-items: center;
    justify-content: center;
    gap: 20px;
  }
  .card {
    width: 820px;
    height: 469px;
    border-radius: 18px;
    background: linear-gradient(180deg, var(--card-top) 0%, var(--card-bottom) 100%);
    display: flex;
    flex-direction: column;
    align-items: center;
    text-align: center;
  }
  .card-back { justify-content: center; }
  .card-back .brand-name {
    font-size: 40px;
    font-weight: 400;
    color: var(--brand-blue);
    margin-top: 30px;
  }
  .card-back .website {
    margin-top: 60px;
    font-size: 22px;
    letter-spacing: 2px;
    color: var(--ink);
  }
  .card-front { padding-top: 52px; }
  .brand-square {
    width: 34px;
    height: 34px;
    background: var(--brand-blue);
  }
  .card-front .brand-name {
    margin-top: 20px;
    font-size: 36px;
    color: var(--brand-blue);
    line-height: 1;
  }
  .tagline {
    margin-top: 6px;
    font-size: 19px;
    color: var(--ink);
    letter-spacing: 1px;
  }
  .person-name {
    margin-top: 26px;
    font-size: 29px;
    color: var(--brand-blue);
    line-height: 1;
  }
  .person-title {
    margin-top: 6px;
    font-size: 19px;
    color: var(--ink);
  }
  .address {
    margin-top: 30px;
    font-size: 18px;
    color: var(--ink-soft);
  }
  .phones {
    margin-top: 4px;
    font-size: 18px;
    color: var(--ink-soft);
  }
  .phones .label { color: var(--brand-blue); font-weight: 600; }
  .phones span + span { margin-left: 14px; }
  .email {
    margin-top: 4px;
    font-size: 15px;
    color: var(--ink-soft);
  }
  .email .domain { color: var(--brand-blue); }
</style>
</head>
<body>
  <section class="card card-back">
    <div class="brand-name">Marlow Holdings</div>
    <div class="website">www.marlowholdingsllc.example</div>
  </section>

  <section class="card card-front">
    <div class="brand-square"></div>
    <div class="brand-name">Marlow Holdings</div>
    <div class="tagline">Foundations for Tomorrow</div>
    <div class="person-name">Derek P. Hollins</div>
    <div class="person-title">President/CEO</div>
    <div class="address">248 West Penrose Street, Suite 2360, Milwaukee, WI 53217</div>
    <div class="phones">
      <span><span class="label">P:</span> 414.555.0142</span>
      <span><span class="label">C:</span> 414.555.0187</span>
      <span><span class="label">F:</span> 414.555.0143</span>
    </div>
    <div class="email">dhollins@<span class="domain">marlowholdingsllc.example</span></div>
  </section>
</body>
</html>
```